Photographer's price list

I am a photographer who runs a studio (Ferrowick Studio) and need to have a document to send clients detailing my packages (collections) and prices. I have written the text in a word document and need a designer to lay it out for me using my logo and two specific fonts: DejaVu Sans and LainieDaySH.

The look should be clean and modern and keep in the same style as my logo. I will primarily be using the final product as a PDF file to email to potential clients. It should stay black and white.

I would also like to be able to update the text myself as my prices and packages change. So I would like a PSD file.

I think I would like for the document to be in landscape format with "Collections" on one side and A la Carte on the other, but I am open to other ideas.

As for sizing, it should be a standard size so that clients can print it out if they like.

Industry/Entity Type

Landscape

Requirements
Must have
• my logo
fonts: DejaVu and LainieDaySH
Easy to email
Easy to display on one page upon opening
Standard size so that printing from a home computer is easy to do.

```html
<!DOCTYPE html>
<html lang="en">
<head>
<meta charset="utf-8">
<title>Ferrowick Studio – 2013 Photography Collections</title>
<link href="https://fonts.googleapis.com/css2?family=Allura&family=Noto+Sans:wght@400;700&display=swap" rel="stylesheet">
<style>
:root{
  --backdrop:#6b6b6b;
  --sheet-grey:#c9c9c9;
  --ink:#1f1f1f;
  --black:#222;
  --white:#fff;
  --photo-dark:#5a5a5a;
  --photo-light:#dcdcdc;
  --silver-a:#f2f2f2;
  --silver-b:#8d8d8d;
  --page-grad-a:#ffffff;
  --page-grad-b:#d6d6d6;
}
*{margin:0;padding:0;box-sizing:border-box}
html,body{width:775px;height:1200px;overflow:hidden;background:var(--backdrop)}
body{position:relative;font-family:"Noto Sans",sans-serif;color:var(--ink)}
.script{font-family:"Allura",cursive;font-weight:400}

/* cover spread */
.cover{position:absolute;left:17px;top:17px;width:741px;height:573px;background:var(--white);overflow:hidden}
.cover-back{position:absolute;left:0;top:0;width:371px;height:507px;background:var(--sheet-grey)}
.cover-spine-bar{position:absolute;left:336px;top:0;width:35px;height:172px;background:var(--black)}
.cover-photo{position:absolute;left:371px;top:0;width:370px;height:172px;
  background:linear-gradient(100deg,var(--photo-light) 0%,var(--photo-dark) 45%,#8a8a8a 70%,var(--photo-light) 100%)}
.cover-band{position:absolute;left:0;top:507px;width:741px;height:66px;background:var(--black)}
.contact{position:absolute;left:0;width:371px;top:433px;text-align:center;font-size:9.5px;line-height:12px}
.contact strong{display:block;font-weight:700}
.brand{position:absolute;left:540px;top:275px;width:170px;display:flex;align-items:center;gap:8px}
.brand-dot{width:12px;height:12px;border-radius:50%;background:var(--ink);flex:none}
.brand-name{font-size:12px;letter-spacing:1.5px;color:var(--ink);white-space:nowrap}
.cover-year{position:absolute;right:48px;top:402px;font-size:40px;line-height:1}
.cover-title{position:absolute;right:48px;top:446px;font-size:36px;line-height:1;white-space:nowrap}

/* price spread */
.prices{position:absolute;left:17px;top:612px;width:741px;height:573px;
  background:linear-gradient(90deg,var(--page-grad-b) 0%,var(--page-grad-a) 40%,var(--page-grad-a) 60%,var(--page-grad-b) 100%);overflow:hidden}
.collection{position:absolute;left:30px;width:310px;height:93px;background:var(--black);border-radius:9px;color:var(--white);text-align:center;padding:3px 30px 0 30px;overflow:hidden}
.collection h2{font-size:25px;line-height:25px;margin-left:40px}
.collection p{font-size:8.3px;line-height:10px;color:#e6e6e6}
.price-tab{position:absolute;left:-22px;top:7px;width:120px;height:22px;transform:rotate(-18deg);
  background:linear-gradient(90deg,var(--silver-a) 0%,#cfcfcf 55%,var(--silver-b) 100%);
  font-size:11px;font-weight:700;color:var(--ink);line-height:22px;text-align:left;padding-left:30px}
.includes{position:absolute;left:30px;width:310px;top:460px;text-align:center;padding:0 26px}
.includes h3{font-size:24px;line-height:24px}
.includes p{font-size:8px;line-height:9.6px}
.alacarte{position:absolute;left:398px;width:320px;top:26px;text-align:center;font-size:10px;line-height:11.3px}
.alacarte h3{font-size:25px;line-height:26px;margin-top:14px}
.alacarte h3:first-child{margin-top:0}
.alacarte .cost{font-family:"Allura",cursive;font-size:14px}
</style>
</head>
<body>

<section class="cover">
  <div class="cover-back"></div>
  <div class="cover-spine-bar"></div>
  <div class="cover-photo" role="img" aria-label="Black and white family portrait photograph"></div>
  <div class="cover-band"></div>
  <div class="contact">
    <strong>Contact Information</strong>
    Mara Holloway<br>+49 170 555 0142<br>Lindenau, 04177<br>Germany
  </div>
  <div class="brand">
    <span class="brand-dot"></span>
    <span class="brand-name">FERROWICK STUDIO</span>
  </div>
  <div class="cover-year script">2013</div>
  <div class="cover-title script">photography collections</div>
</section>

<section class="prices">
  <article class="collection" style="top:34px">
    <div class="price-tab">300 €</div>
    <h2 class="script">Collection 1</h2>
    <p>Your favorite five images from the session will be professionally edited and presented to you on disk as high resolution jpegs</p>
  </article>
  <article class="collection" style="top:139px">
    <div class="price-tab">400 €</div>
    <h2 class="script">Collection 2</h2>
    <p>Your favorite ten images from the session will be professionally edited and given to you on disk as high resolution jpegs.<br>Your favorite image from the session will be professionally printed for you (20x30cm) on Lindenmühle paper, Mara's favorite for portraits.</p>
  </article>
  <article class="collection" style="top:247px">
    <div class="price-tab">500 €</div>
    <h2 class="script">Collection 3</h2>
    <p>Your favorite fifteen images from the session will be professionally edited and presented to you on disk as high resolution jpegs.<br>Your favorite two images from the session will be professionally printed for you (20x30cm) on Lindenmühle paper, Mara's favorite for portraits.</p>
  </article>
  <article class="collection" style="top:354px">
    <div class="price-tab">600 €</div>
    <h2 class="script">Collection 4</h2>
    <p><u>ALL</u> presented images from the session will be professionally edited and presented to you on disk as high resolution jpegs (approximately 40+ images).<br>Your favorite two images from the session will be professionally printed for you (20x30cm) on Lindenmühle paper, Mara's favorite for portraits.</p>
  </article>

  <div class="includes">
    <h3 class="script">all collections include</h3>
    <p>One to two hour portrait session with photographer in location of your choice (unlimited time if necessary!)<br>Mara will create a presentation video with hand-selected music and custom editing, which tells your story, highlights the best images, and reveals the connections within your family.<br>An online gallery for viewing and ordering helps you share your images with family and friends.</p>
  </div>

  <div class="alacarte">
    <h3 class="script">a la carte pricing</h3>
    <p>These products may be purchased separately to complement your collection. A consultation with Mara will help you decide which products are best for gifts and for your home.</p>
    <h3 class="script">high resolution digital images</h3>
    <p>Perfect if you just need to add “one more image” to your collection!<br>High-resolution jpeg file <span class="cost">25 €</span> each</p>
    <h3 class="script">matt prints</h3>
    <p>20x30 cm and smaller <span class="cost">25 €</span><br>Each print is professionally edited, printed on archival photo paper.<br>Purchase includes the JPEG file for your personal digital use.</p>
    <h3 class="script">lindenmühle prints</h3>
    <p>Prints on Lindenmühle (watercolor) paper are Mara's favorite for large format color prints<br>30x40 cm <span class="cost">45 €</span></p>
    <h3 class="script">canvas prints</h3>
    <p>Ready-to-hang, stretched canvas wall art of your favorite images<br>30x40 cm <span class="cost">100 €</span></p>
    <h3 class="script">framed + matted prints</h3>
    <p>Beautiful Lindenmühle prints finished with wide mats and simple, elegant frames of your choice<br>30x40 inch <span class="cost">350 €</span></p>
    <h3 class="script">custom designed albums</h3>
    <p>Images from your session are selected for the custom design of an album and bound in a book for a modern presentation of your images. There are a number of cover choices for the classic flush-mount and beautifully crafted albums. A great way to display all of your favorite images from your session on your coffee table.<br>Prices begin at <span class="cost">300 €</span></p>
  </div>
</section>

</body>
</html>
```